Kestrel Forge Tech
Bus. Cards/Stationary/Presentation
Kestrel Forge Tech - Information Technology
Creative Brief
Use specific fonts
Open to ideas on font pairing
Professional
Wendell Pask
Owner
218 Larkspur Avenue Suite 4400 Beaumont, TX 77701
Wendell.Pask@kestrelforgetech.com
www.kestrelforgetech.com
I am open to my logo displayed on the back. I am also open to ideas on the back of business card. Be creative on front and back.

```html
<!DOCTYPE html>
<html lang="en">
<head>
<meta charset="utf-8">
<title>Kestrel Forge Tech – Presentation Template</title>
<link href="https://fonts.googleapis.com/css2?family=Open+Sans:wght@400;600;700&display=swap" rel="stylesheet">
<style>
  :root{
    --backdrop:#2a2a2a;
    --slide:#ffffff;
    --green:#6cc13a;
    --ink:#4d4d4d;
    --ink-soft:#8a8a8a;
    --rule:#d6d6d6;
    --bar-grey:#a3a3a3;
    --faint:#eef5e8;
  }
  *{box-sizing:border-box;margin:0;padding:0}
  html,body{width:1200px;height:939px;overflow:hidden}
  body{background:var(--backdrop);font-family:"Open Sans",Arial,sans-serif;color:var(--ink);position:relative}
  .slide{position:absolute;width:523px;height:383px;background:var(--slide);overflow:hidden;box-shadow:0 4px 14px rgba(0,0,0,.45)}
  .slide--title{left:51px;top:51px}
  .slide--list{left:607px;top:51px}
  .slide--chart{left:51px;top:467px}
  .slide--closing{left:607px;top:467px}
  .deco-circle{position:absolute;border-radius:50%;background:var(--faint)}
  .wordmark{display:flex;align-items:center;gap:10px;font-weight:700;color:var(--ink);white-space:nowrap}
  .wordmark__dot{width:22px;height:22px;border-radius:50%;background:var(--green);flex:none}
  .slide--title .wordmark{position:absolute;left:0;right:0;top:118px;justify-content:center;font-size:30px}
  .pres-title{position:absolute;left:0;right:0;top:212px;text-align:center;color:var(--green);font-weight:700;font-size:18px}
  .pres-sub{position:absolute;left:0;right:0;top:238px;text-align:center;font-size:13px;color:var(--ink)}
  .slide-head{position:absolute;left:36px;top:30px}
  .slide-head h2{color:var(--green);font-size:16px;font-weight:700;letter-spacing:.2px}
  .slide-head p{font-size:10px;color:var(--ink);margin-top:1px}
  .group{position:absolute;width:185px;display:flex;gap:7px}
  .group__icon{flex:none;width:13px;height:13px;border-radius:50%;border:2px solid var(--ink-soft);position:relative;margin-top:1px}
  .group__icon::after{content:"";position:absolute;left:2px;top:2px;width:5px;height:5px;border-radius:50%;background:var(--green)}
  .group h3{font-size:9px;font-weight:700;color:var(--ink)}
  .group p{font-size:7px;line-height:1.35;color:var(--ink-soft)}
  .media-box{position:absolute;left:36px;top:178px;width:150px;height:78px;background:linear-gradient(180deg,#f4f4f4,#c9c9c9);border:1px solid var(--rule)}
  .chart{position:absolute;left:30px;top:88px}
  .slide--closing .wordmark{position:absolute;left:150px;top:222px;font-size:30px}
</style>
</head>
<body>

<section class="slide slide--title">
  <div class="wordmark"><span class="wordmark__dot"></span>Kestrel Forge Tech</div>
  <h1 class="pres-title">TITLE OF PRESENTATION</h1>
  <p class="pres-sub">Description</p>
</section>

<section class="slide slide--list">
  <div class="deco-circle" style="left:330px;top:40px;width:260px;height:260px"></div>
  <header class="slide-head"><h2>SAMPLES OF CONTENT LIST</h2><p>Description in this line</p></header>
  <div class="group" style="left:36px;top:82px"><span class="group__icon"></span><div><h3>Group 3</h3><p>Short summary of this group and its key points for the audience.</p></div></div>
  <div class="group" style="left:36px;top:128px"><span class="group__icon"></span><div><h3>Group 4</h3><p>Short summary of this group and its key points for the audience.</p></div></div>
  <div class="media-box"></div>
  <div class="group" style="left:300px;top:82px"><span class="group__icon"></span><div><h3>Group 3</h3><p>Short summary of this group and its key points for the audience.</p></div></div>
  <div class="group" style="left:300px;top:128px"><span class="group__icon"></span><div><h3>Group 4</h3><p>Short summary of this group and its key points for the audience.</p></div></div>
  <div class="group" style="left:300px;top:174px"><span class="group__icon"></span><div><h3>Group 5</h3><p>Short summary of this group and its key points for the audience.</p></div></div>
  <div class="group" style="left:300px;top:220px"><span class="group__icon"></span><div><h3>Group 6</h3><p>Short summary of this group and its key points for the audience.</p></div></div>
</section>

<section class="slide slide--chart">
  <div class="deco-circle" style="left:360px;top:-40px;width:260px;height:260px"></div>
  <header class="slide-head"><h2>SAMPLES OF CONTENT LIST</h2><p>Description in this line</p></header>
  <svg class="chart" width="210" height="240" viewBox="0 0 210 240" aria-label="Bar chart comparing four groups">
    <g stroke="#dcdcdc" stroke-width="1">
      <line x1="20" y1="10" x2="205" y2="10"/><line x1="20" y1="50" x2="205" y2="50"/>
      <line x1="20" y1="90" x2="205" y2="90"/><line x1="20" y1="130" x2="205" y2="130"/>
      <line x1="20" y1="170" x2="205" y2="170"/>
    </g>
    <line x1="20" y1="5" x2="20" y2="210" stroke="#9a9a9a"/>
    <line x1="20" y1="210" x2="205" y2="210" stroke="#9a9a9a"/>
    <rect x="30" y="18" width="30" height="192" fill="#6cc13a"/>
    <rect x="73" y="140" width="30" height="70" fill="#a3a3a3"/>
    <rect x="116" y="180" width="30" height="30" fill="#6cc13a"/>
    <rect x="159" y="185" width="30" height="25" fill="#a3a3a3"/>
    <g font-family="Open Sans, Arial, sans-serif" font-size="6" fill="#4d4d4d" text-anchor="middle">
      <text x="45" y="220">Group 1</text><text x="88" y="220">Group 2</text>
      <text x="131" y="220">Group 3</text><text x="174" y="220">Group 4</text>
    </g>
  </svg>
  <div class="group" style="left:280px;top:90px"><span class="group__icon"></span><div><h3>Group 3</h3><p>Short summary of this group and its key points for the audience.</p></div></div>
  <div class="group" style="left:280px;top:142px"><span class="group__icon"></span><div><h3>Group 4</h3><p>Short summary of this group and its key points for the audience.</p></div></div>
  <div class="group" style="left:280px;top:194px"><span class="group__icon"></span><div><h3>Group 5</h3><p>Short summary of this group and its key points for the audience.</p></div></div>
  <div class="group" style="left:280px;top:246px"><span class="group__icon"></span><div><h3>Group 6</h3><p>Short summary of this group and its key points for the audience.</p></div></div>
</section>

<section class="slide slide--closing">
  <div class="deco-circle" style="left:300px;top:-60px;width:300px;height:300px"></div>
  <div class="wordmark"><span class="wordmark__dot"></span>Kestrel Forge Tech</div>
</section>

</body>
</html>
```